Fall BVTS Postcard Design

I own Birchwood Valley Tumbling School. We offer gymnastics classes to children ages 18vmonth to 18 years. We have a competitive team, an after school program and many day camps along with added on workshops. We will be offering two work shops this fall: Spanish Gymnastics... A class taught all in Spanish. Our second work shop will be Hip Hop Gymnastics.

I need a card that lets people know we are MORE than just gymnastics. We offer active options for children after school every day of the week and we are affordable. I want the front to be bright, fun and colorful and the back to have the schedule of classes we offer. I would like the front to drive people to our website: www.bvtsgym.example or e-mail: info@bvtsgym.example
I would like to front to offer a "Free Trial Class" *The details will be they can try it risk free, if they sign up then they pay for it as their start date. If not, no charge. Also, our after school program, sign up for 4 days get the 5th FREE! *For those who sign up for a month at a time. I have also added pictures of the gym. They are not necessary to have on the card, but put there as an option.

Our listed Mission Statement:
BVTS is dedicated to keeping kids moving! We are focused on allowing kids of all ages to be active and to have fun doing it. We encourage our students to learn gymnastics safely, while increasing self-confidence, body awareness, coordination, and skill. Children of all ages will build strength, increase flexibility, agility, balance and mental focus, while also learning how to incorporate overall fitness into a healthy lifestyle for years to come. We want to appropriately challenge each student and help them meet personal goals, while maintaining a happy and healthy environment for all.

Requirements
Must have
• Our gym Logo which is attached as the "BVTS Letter head" file.
Our contact info: www.bvtsgym.example ~ Info@bvtsgym.example ~ (555) 417-2096
Our class schedule on the back.
After School Program Begins: August 26th
Classes start: September 8th
"Stars" or "Bursts" on the Front with the "Free" listed on them, with an asterisk with it for the details on the back that really let you see the FREE
Must fit for a "over-sized card" looking to do 8.52"x5.47" size card
Nice to have
• A fun background picture on the front. It could be my gym or just fun bright with a "kid" having fun on it, upside down or whatever. I do not want "cluttered".
My gym colors are Black, Red and Gold but not necessary to use that color scheme.

```html
<!DOCTYPE html>
<html lang="en">
<head>
<meta charset="utf-8">
<title>BVTS Fall Postcard</title>
<link rel="stylesheet" href="https://fonts.googleapis.com/css2?family=Bebas+Neue&family=Lato:wght@400;700;900&display=swap">
<style>
:root{
  --red:#a8200d;
  --ink:#231f20;
  --black:#111;
  --gold:#f2e21c;
  --white:#fff;
  --page:#e9e6e2;
  --line:#222;
  --hl:#efe44a;
}
*{box-sizing:border-box;margin:0;padding:0}
html,body{width:921px;height:1200px;overflow:hidden}
body{background:var(--page);position:relative;font-family:"Lato",Arial,sans-serif}
.display{font-family:"Bebas Neue","Oswald",sans-serif;font-weight:400}

/* ---------- front ---------- */
.card-front{position:absolute;left:60px;top:64px;width:786px;height:504px;background:var(--white);overflow:hidden}
.hero-photo{position:absolute;left:285px;top:0;width:501px;height:282px;
  background:linear-gradient(135deg,#d8dde6 0%,#c9392e 28%,#e6c21c 42%,#2f5fb4 58%,#3c9a4a 72%,#d9d4cf 100%)}
.logo-banner{position:absolute;left:20px;top:6px;width:262px;height:110px}
.logo-banner svg{position:absolute;inset:0}
.logo-name{position:absolute;left:0;right:0;top:30px;text-align:center;color:var(--white);
  font-family:"Lato",sans-serif;font-weight:700;font-size:15px;line-height:19px;letter-spacing:.5px}
.logo-dot{position:absolute;left:125px;top:12px;width:12px;height:12px;border-radius:50%;background:var(--white)}
.tagline{position:absolute;left:0;top:128px;width:285px;height:102px;background:var(--red);
  color:var(--white);font-size:37px;line-height:102px;padding-left:14px;white-space:nowrap;overflow:hidden}
.front-panel{position:absolute;left:0;top:0;width:786px;height:456px}
.front-copy{position:absolute;left:16px;top:252px;width:760px;color:var(--white)}
.camp-title{font-size:38px;line-height:40px;letter-spacing:.5px}
.dates{font-size:33px;line-height:44px;letter-spacing:.3px}
.dates .hi{color:var(--gold);font-size:44px}
.mission{margin-top:8px;font-family:"Bebas Neue",sans-serif;font-size:11.6px;line-height:17px;letter-spacing:.45px}
.offer{margin-top:9px;font-size:12.5px;line-height:19px}
.contact-bar{position:absolute;left:0;top:459px;width:786px;height:45px}
.contact{position:absolute;top:0;height:45px;display:flex;align-items:center;justify-content:center;gap:8px;
  color:var(--white);font-weight:700;font-size:20px;white-space:nowrap}
.contact svg{flex:none}
.contact.web{left:0;width:253px;background:var(--red)}
.contact.mail{left:261px;width:261px;background:var(--ink)}
.contact.phone{left:528px;width:258px;background:var(--red)}

/* ---------- back ---------- */
.card-back{position:absolute;left:58px;top:628px;width:792px;height:508px;background:var(--white);overflow:hidden}
.schedule{position:absolute;left:0;top:13px;width:437px;border-collapse:collapse;table-layout:fixed}
.schedule td,.schedule th{border:1px solid var(--line);font-size:7.4px;line-height:9px;text-align:center;padding:0 1px;white-space:nowrap}
.schedule td.cls{border-left:none;text-align:left;color:var(--red);font-weight:900;font-size:9px;padding-left:15px;white-space:nowrap;line-height:10px}
.schedule tbody tr{height:13.5px}
.schedule tbody tr.tall{height:22px}
.schedule thead tr{height:24px}
.schedule thead th{border:none;border-left:3px solid var(--white);color:var(--white);font-family:"Bebas Neue",sans-serif;font-weight:400;font-size:14px;line-height:24px}
.schedule thead th.dark{background:var(--black)}
.schedule thead th.red{background:var(--red)}
.schedule thead th.class-head{background:none;border-left:none;position:relative;text-align:left}
.class-tab{position:absolute;left:0;top:0;width:115px;height:24px}
.class-tab span{position:absolute;left:36px;top:0;line-height:24px;font-size:17px;color:var(--white)}
.schedule .ws{background:var(--hl)}
.team-note{position:absolute;left:16px;top:422px;font-size:16px;line-height:18px;color:var(--ink);letter-spacing:.3px;white-space:nowrap}
.fine-print{position:absolute;left:16px;top:442px;width:420px;font-family:"Bebas Neue",sans-serif;font-size:9px;line-height:10px;color:var(--red)}
.back-logo{position:absolute;left:462px;top:56px;width:160px;text-align:center;color:var(--ink);font-weight:700;font-size:13px;line-height:17px}
.back-logo .logo-dot{position:static;display:block;margin:0 auto 6px;background:var(--ink)}
.trial-sticker{position:absolute;left:630px;top:16px;width:160px;height:160px}
.trial-text{position:absolute;left:628px;top:60px;width:150px;text-align:center;color:var(--white);
  font-size:28px;line-height:26px;transform:rotate(-48deg)}
.ribbon{position:absolute;right:0;color:var(--white);text-align:right;padding-right:16px}
.ribbon svg{position:absolute;left:0;top:0;z-index:0}
.ribbon > div{position:relative;z-index:1}
.ribbon h3{font-family:"Bebas Neue",sans-serif;font-weight:400;font-size:22px;line-height:22px;letter-spacing:.3px}
.ribbon p{font-weight:700;font-size:14px;line-height:17px}
.ribbon .gold{color:var(--gold);font-size:17px}
.ribbon.party{top:184px;width:336px;height:70px;padding-top:9px}
.ribbon.self{top:274px;width:336px;height:82px;padding-top:10px}
.ribbon.night{top:364px;width:262px;height:76px;padding-top:8px}
.back-bar{position:absolute;left:0;top:475px;width:792px;height:33px}
.back-bar span{position:absolute;top:0;height:33px}
.back-bar .b1{left:0;width:258px;background:var(--red)}
.back-bar .b2{left:263px;width:272px;background:var(--black)}
.back-bar .b3{left:540px;width:252px;background:var(--red)}
</style>
</head>
<body>

<section class="card-front">
  <div class="hero-photo" role="img" aria-label="Gym interior with a colourful inflatable castle slide and tumbling mats"></div>

  <svg class="front-panel" width="786" height="456" viewBox="0 0 786 456" aria-hidden="true">
    <polygon points="0,232 410,232 416,294 786,294 786,456 0,456" fill="#231f20"/>
    <polyline points="0,232 410,232 416,288 786,288" fill="none" stroke="#fff" stroke-width="5"/>
  </svg>

  <div class="logo-banner">
    <svg width="262" height="110" viewBox="0 0 262 110" aria-hidden="true">
      <polygon points="0,0 262,0 262,84 131,108 0,84" fill="#231f20"/>
    </svg>
    <span class="logo-dot"></span>
    <div class="logo-name">Birchwood Valley<br>Tumbling School</div>
  </div>

  <div class="tagline display">Keeping Kids Moving</div>

  <div class="front-copy">
    <h1 class="camp-title display">After School Mini Camp</h1>
    <p class="dates display"><span class="hi">August 26th</span> Classes Start: <span class="hi">September 8th</span></p>
    <p class="mission">BVTS is dedicated to keeping kids moving! We are focused on allowing kids of all ages to be active and to have fun doing it. We encourage our students to learn gymnastics safely, while increasing self-confidence, body awareness, coordination, and skill. Children of all ages will build strength, increase flexibility, agility, balance and mental focus, while also learning how to incorporate overall fitness into a healthy lifestyle for years to come.</p>
    <p class="offer">*Try it risk free, if they sign up then they pay for it as their start date. If not, no charge. Also, our after school program, sign up for 4 days get the 5th FREE!</p>
  </div>

  <div class="contact-bar">
    <div class="contact web">
      <svg width="18" height="18" viewBox="0 0 20 20" aria-hidden="true"><g fill="none" stroke="#fff" stroke-width="1.8"><circle cx="10" cy="10" r="8"/><ellipse cx="10" cy="10" rx="3.5" ry="8"/><line x1="2" y1="10" x2="18" y2="10"/></g></svg>
      www.bvtsgym.example
    </div>
    <div class="contact mail">
      <svg width="24" height="16" viewBox="0 0 24 16" aria-hidden="true"><rect x="1" y="1" width="22" height="14" fill="#fff"/><polyline points="1,1 12,9 23,1" fill="none" stroke="#231f20" stroke-width="1.6"/></svg>
      Info@bvtsgym.example
    </div>
    <div class="contact phone">
      <svg width="18" height="18" viewBox="0 0 18 18" aria-hidden="true"><rect width="18" height="18" rx="3" fill="#fff"/><path d="M5 4c1-1 2 0 2.4 1.3l.5 1.3c.2.6-.6 1.1-.8 1.4.7 1.5 1.6 2.4 3 3 .4-.3.8-1 1.4-.8l1.3.5C14 11 15 12 14 13c-1 1.2-3.5 1-6-1.5S3.8 5 5 4z" fill="#a8200d"/></svg>
      (555) 417-2096
    </div>
  </div>
</section>

<section class="card-back">
  <table class="schedule">
    <colgroup><col style="width:116px"><col span="7" style="width:45.8px"></colgroup>
    <thead>
      <tr>
        <th class="class-head"><svg class="class-tab" width="115" height="24" viewBox="0 0 115 24" aria-hidden="true"><polygon points="0,0 106,0 115,12 106,24 0,24" fill="#a8200d"/></svg><span class="class-tab"><span class="display">Class</span></span></th>
        <th class="dark">Mon</th><th class="red">Tue</th><th class="dark">Wed</th><th class="red">Thurs</th><th class="dark">Fri</th><th class="red">Sat</th><th class="dark">Sun</th>
      </tr>
    </thead>
    <tbody>
      <tr><td class="cls ws">* Spanish Gym W.S.</td><td></td><td></td><td></td><td class="ws">9:15-10:00</td><td></td><td></td><td></td></tr>
      <tr><td class="cls ws">* Hip Hop Gym</td><td></td><td></td><td></td><td></td><td class="ws">3:30-4:30</td><td></td><td></td></tr>
      <tr><td class="cls">MOM, POP &amp; TOT</td><td></td><td>5:00-5:45</td><td></td><td>11-11:45</td><td></td><td>9:00-9:45</td><td></td></tr>
      <tr><td class="cls">PRE-K</td><td></td><td>4-4:50</td><td></td><td>10:05-10:55</td><td></td><td>10:00-10:50</td><td></td></tr>
      <tr><td class="cls"></td><td></td><td>5-5:50</td><td></td><td></td><td></td><td></td><td></td></tr>
      <tr><td class="cls"></td><td></td><td>5:50-6:40</td><td></td><td></td><td></td><td></td><td></td></tr>
      <tr><td class="cls"></td><td></td><td></td><td></td><td></td><td></td><td></td><td></td></tr>
      <tr><td class="cls">KINDERGYM</td><td></td><td>3:15-4:05</td><td></td><td></td><td></td><td>10:00-10:50</td><td></td></tr>
      <tr><td class="cls"></td><td></td><td>5-5:50</td><td></td><td></td><td></td><td></td><td></td></tr>
      <tr><td class="cls"></td><td></td><td>5:50-6:40</td><td></td><td></td><td></td><td></td><td></td></tr>
      <tr><td class="cls"></td><td></td><td></td><td></td><td></td><td></td><td></td><td></td></tr>
      <tr><td class="cls">BEGINNER I</td><td>3:15-4:15</td><td></td><td></td><td>4:00-5:00</td><td></td><td>11:00-12:00</td><td></td></tr>
      <tr><td class="cls"></td><td>4:15-5:15</td><td></td><td></td><td></td><td></td><td></td><td></td></tr>
      <tr><td class="cls"></td><td>5:15-6:15</td><td></td><td></td><td></td><td></td><td></td><td></td></tr>
      <tr><td class="cls">BEGINNER II</td><td>5:15-6:30</td><td></td><td>3:15-4:30</td><td>5:00-6:15</td><td></td><td>11:00-12:15</td><td></td></tr>
      <tr><td class="cls">Int./Adv</td><td></td><td></td><td></td><td>5:00-6:30</td><td>4:30-6:00</td><td>11:00-12:30</td><td></td></tr>
      <tr class="tall"><td class="cls">BOYS 6 &amp; up</td><td></td><td></td><td>4:30-5:30<br>5:30-6:30</td><td></td><td></td><td></td><td></td></tr>
      <tr class="tall"><td class="cls">MIDDLE SCHOOL<br>/ H.S.</td><td></td><td></td><td></td><td></td><td></td><td></td><td></td></tr>
      <tr><td class="cls">BOYS TEAM all ages</td><td></td><td></td><td>4:30-6:30</td><td></td><td></td><td></td><td></td></tr>
      <tr class="tall"><td class="cls">Parent &amp; Tot<br>&nbsp;Open Gym</td><td>10-11:30</td><td></td><td></td><td></td><td>10-11:30</td><td></td><td></td></tr>
      <tr class="tall"><td class="cls">After School Camp</td><td>3:00-5:00</td><td>3:00-5:00</td><td>3:00-5:00</td><td>3:00-5:00</td><td>3:00-5:00</td><td></td><td></td></tr>
      <tr class="tall"><td class="cls">RVSU Early Rel.<br>Camp</td><td></td><td></td><td>12:30-5:00</td><td></td><td></td><td></td><td></td></tr>
      <tr><td class="cls">Birthday Parties</td><td></td><td></td><td></td><td></td><td></td><td>4:00-5:30</td><td>4:00-5:30</td></tr>
      <tr><td class="cls"></td><td></td><td></td><td></td><td></td><td></td><td>6:00-7:30</td><td>6:00-7:30</td></tr>
    </tbody>
  </table>

  <p class="team-note display">For team scheudle please see the webiste or check in with Marisa</p>
  <p class="fine-print">* Will run 4 weeks at a time as a work shop. Priced differently then regular running classes. Will change classes offered throughout the year.</p>

  <div class="back-logo"><span class="logo-dot"></span>Birchwood Valley<br>Tumbling School</div>

  <svg class="trial-sticker" width="160" height="160" viewBox="0 0 160 160" aria-hidden="true">
    <circle cx="80" cy="80" r="76" fill="#e9df1e"/>
    <circle cx="80" cy="80" r="76" fill="none" stroke="#c9be10" stroke-width="2"/>
    <path d="M118 142 L150 110 Q128 112 118 142 Z" fill="#f4f4f4"/>
  </svg>
  <div class="trial-text display">Free Trial<br>Class</div>

  <div class="ribbon party">
    <svg width="336" height="70" viewBox="0 0 336 70" aria-hidden="true"><polygon points="28,0 336,0 336,70 28,70 0,35" fill="#a8200d"/></svg>
    <div>
      <h3>Birthday Parties</h3>
      <p><span class="gold">$175</span> for 8 ( <span class="gold">$12</span> for each additional child<br>after 8)<span class="gold">$12</span> each additional pizza</p>
    </div>
  </div>

  <div class="ribbon self">
    <svg width="336" height="82" viewBox="0 0 336 82" aria-hidden="true"><polygon points="30,0 336,0 336,82 30,82 0,41" fill="#111"/></svg>
    <div>
      <h3>Self Supplied Party Includes:</h3>
      <p><span class="gold">$150</span> for 8 (<span class="gold">$10</span> for each additional<br>child after 8)</p>
    </div>
  </div>

  <div class="ribbon night">
    <svg width="262" height="76" viewBox="0 0 262 76" aria-hidden="true"><polygon points="28,0 262,0 262,76 28,76 0,38" fill="#a8200d"/></svg>
    <div>
      <h3>Kids Night Out</h3>
      <p><span class="gold">$30</span> first child2 siblings <span class="gold">$45</span><br>3 siblings <span class="gold">$65</span></p>
    </div>
  </div>

  <div class="back-bar" aria-hidden="true"><span class="b1"></span><span class="b2"></span><span class="b3"></span></div>
</section>

</body>
</html>
```